nutrition company business card

I would like to have a business card that has two sides, one being the green color from the Company name on the logo. I am open to ideas and looks that work with my logo. I like the idea of having a negative image of the tree on the green side.

For my information on the card I must have:
Linda Moorcombe
415-872-6041
lindamoorcombe@quellmail.net

This area will need to be updated once I complete my schooling.

Reason: I need to extend my deadline by one day as I have been sick the last week and not had time to review all the new designs. Thank you.

Industry/Entity Type

Nutrition

Requirements
Must have
• I would like to have a business card that has two sides, one being the green color from the Company name on the logo. I am open to ideas and looks that work with my logo. I like the idea of having a negative image of the tree on the green side.
• For my information on the card I must have:
• Linda Moorcombe
• 415-872-6041
• lindamoorcombe@quellmail.net
• This area will need to be updated once I complete my schooling.

```html
<!DOCTYPE html>
<html lang="en">
<head>
<meta charset="utf-8">
<title>Thriving Tables – Business Card</title>
<link rel="stylesheet" href="https://fonts.googleapis.com/css2?family=Quicksand:wght@400;500&family=Roboto:wght@300;400&display=swap">
<style>
  :root {
    --bg: #dedbd6;
    --brand-green: #76a22a;
    --card-white: #f2f2f2;
    --ink-taupe: #8c7d74;
    --paper: #ffffff;
  }
  * { margin: 0; padding: 0; box-sizing: border-box; }
  html, body { width: 1200px; height: 900px; overflow: hidden; }
  body {
    background: var(--bg);
    position: relative;
    font-family: "Quicksand", sans-serif;
  }
  .card {
    position: absolute;
    width: 600px;
    height: 340px;
    left: 300px;
    box-shadow: 0 6px 18px rgba(0,0,0,0.12);
  }
  .card--front { top: 70px; background: var(--brand-green); }
  .card--back  { top: 490px; background: var(--card-white); }

  .brand {
    position: absolute;
    display: flex;
    flex-direction: column;
    align-items: center;
    gap: 14px;
  }
  .brand__mark {
    width: 92px; height: 92px;
    border-radius: 50%;
    border: 5px solid currentColor;
  }
  .brand__name {
    font-weight: 400;
    font-size: 34px;
    letter-spacing: 0.5px;
    white-space: nowrap;
  }
  .card--front .brand {
    left: 0; right: 0; top: 96px;
    color: var(--paper);
  }
  .card--back .brand {
    left: 50px; top: 110px; width: 260px;
    color: var(--brand-green);
  }
  .card--back .brand__mark { border-color: var(--ink-taupe); width: 84px; height: 84px; }
  .card--back .brand__name { font-size: 28px; }

  .divider {
    position: absolute;
    left: 340px; top: 70px;
    width: 1.5px; height: 120px;
    background: var(--brand-green);
  }
  .contact {
    position: absolute;
    left: 372px; top: 80px;
    font-family: "Roboto", sans-serif;
    color: var(--ink-taupe);
  }
  .contact__name {
    font-weight: 300;
    font-size: 19px;
    text-transform: uppercase;
    margin-bottom: 34px;
  }
  .contact__row {
    display: flex;
    gap: 10px;
    font-weight: 300;
    font-size: 13px;
    line-height: 19px;
  }
  .contact__label { color: var(--brand-green); width: 10px; }
</style>
</head>
<body>
  <section class="card card--front" aria-label="Card front">
    <div class="brand">
      <span class="brand__mark"></span>
      <span class="brand__name">Thriving Tables</span>
    </div>
  </section>

  <section class="card card--back" aria-label="Card back">
    <div class="brand">
      <span class="brand__mark"></span>
      <span class="brand__name">Thriving Tables</span>
    </div>
    <div class="divider"></div>
    <div class="contact">
      <p class="contact__name">Linda Moorcombe</p>
      <p class="contact__row"><span class="contact__label">T</span><span>415-872-6041</span></p>
      <p class="contact__row"><span class="contact__label">E</span><span>lindamoorcombe@quellmail.net</span></p>
    </div>
  </section>
</body>
</html>
```